Open house postcard

Please create a postcard with the details of our open house for our indoor golf facility:

Open House March 10th 1:00-4:00pm
1847 W. Dalton Ave
Unit C7
Millbrook, OH 45308
www.fairpinlinks.com
email: info@fairpinlinks.com

We work with serious golfers and those that want to be serious golfers…
to make you better, faster, at all phases of the game…
We use the same state-of-the-art technology as professional golfers…
which produces data sets that shows your improvement in real time.
Our facility is available 24/7 to our members, which allows you to improve on your time.

Open house special: Complimentary evaluations instead of $200
*You can email us before the open house to schedule your complimentary evaluation or initial practice session

Target Market(s)

Golfers

Font styles to use
Serif

Colors
ec1f27
1b1b1b
757575
cacaca
ffffff

Requirements
Must have
• Date and time
• address
• description
• Open house special: Complimentary evaluations instead of $200
• *Limited memberships offered. You can email us before the open house to schedule your complimentary evaluation or practice session

```html
<!DOCTYPE html>
<html lang="en">
<head>
<meta charset="utf-8">
<title>Fairpin Links – Open House Postcard</title>
<link href="https://fonts.googleapis.com/css2?family=Open+Sans:ital,wght@0,400;0,600;0,700;1,400&display=swap" rel="stylesheet">
<style>
  :root {
    --red: #ec1f27;
    --ink: #1b1b1b;
    --slate: #3a3a3a;
    --grey: #757575;
    --light: #cacaca;
    --paper: #ffffff;
    --backdrop: #e4e4e2;
    --turf: #4f8a4a;
  }
  * { box-sizing: border-box; margin: 0; padding: 0; }
  html, body { width: 1200px; height: 900px; overflow: hidden; }
  body {
    background: var(--backdrop);
    font-family: "Open Sans", Arial, sans-serif;
    position: relative;
  }
  .postcard {
    position: absolute;
    background: var(--paper);
    box-shadow: 0 3px 8px rgba(0,0,0,.25);
    overflow: hidden;
  }
  .postcard-back { left: 60px; top: 48px; width: 552px; height: 368px; }
  .postcard-front { left: 532px; top: 430px; width: 548px; height: 366px; }
  .card-shape { position: absolute; inset: 0; }

  .brand { position: absolute; display: flex; align-items: center; gap: 8px; }
  .brand-ring { border-radius: 50%; border: 3px solid currentColor; flex: none; }
  .brand-name { font-weight: 700; line-height: 1; }
  .brand-tagline { font-weight: 400; margin-top: 2px; white-space: nowrap; }

  /* back */
  .postcard-back .brand { left: 20px; top: 20px; color: var(--paper); }
  .postcard-back .brand-ring { width: 45px; height: 45px; }
  .postcard-back .brand-name { font-size: 27px; }
  .postcard-back .brand-tagline { font-size: 10px; color: var(--light); }
  .description {
    position: absolute; left: 20px; top: 96px; width: 290px;
    color: var(--paper); font-size: 10.5px; line-height: 18.3px; font-weight: 600;
  }
  .date-box {
    position: absolute; border: 2px solid currentColor; border-radius: 7px;
    font-weight: 700; display: flex; align-items: center; justify-content: center; gap: 5px;
    white-space: nowrap;
  }
  .postcard-back .date-box {
    left: 20px; top: 273px; width: 216px; height: 34px;
    color: var(--paper); font-size: 16px;
  }
  .accent { color: var(--red); }
  .postcard-back .email { position: absolute; left: 23px; top: 330px; font-size: 14px; color: var(--paper); }
  .stamp-box {
    position: absolute; left: 474px; top: 4px; width: 60px; height: 70px;
    border: 2px dotted var(--grey);
  }
  .address-line { position: absolute; left: 352px; width: 182px; border-top: 1px solid var(--ink); }
  .mailing-address {
    position: absolute; right: 18px; top: 279px; text-align: right; font-style: normal;
    font-size: 13px; line-height: 18.2px; color: var(--ink);
  }

  /* front */
  .postcard-front .brand { left: 14px; top: 38px; color: var(--red); }
  .postcard-front .brand-ring { width: 58px; height: 58px; }
  .postcard-front .brand-name { font-size: 34px; }
  .postcard-front .brand-tagline { font-size: 12px; }
  .offer-title {
    position: absolute; left: 22px; top: 142px;
    font-size: 22px; font-weight: 700; color: var(--red); letter-spacing: .3px;
  }
  .offer-detail {
    position: absolute; left: 23px; top: 174px;
    font-size: 14px; font-weight: 700; color: var(--ink); line-height: 17px; letter-spacing: .3px;
  }
  .postcard-front .date-box {
    left: 22px; top: 220px; width: 215px; height: 34px;
    color: var(--ink); font-size: 15px;
  }
  .facility-photo { position: absolute; right: 0; top: 0; width: 548px; height: 266px; }
  .notice-band {
    position: absolute; left: 0; top: 266px; width: 100%; height: 64px;
    background: var(--red); color: var(--paper);
    font-style: italic; font-size: 12.5px; line-height: 22px;
    display: flex; align-items: center; justify-content: center; text-align: center; padding: 0 20px;
  }
  .postcard-front .email {
    position: absolute; left: 0; width: 100%; top: 337px; text-align: center;
    font-size: 17px; color: var(--ink);
  }
</style>
</head>
<body>

<section class="postcard postcard-back">
  <svg class="card-shape" viewBox="0 0 552 368" aria-hidden="true">
    <polygon points="0,0 280,0 332,184 280,368 0,368" fill="var(--slate)"/>
    <polyline points="280,0 332,184 280,368" fill="none" stroke="var(--red)" stroke-width="3"/>
  </svg>
  <div class="brand">
    <span class="brand-ring"></span>
    <div>
      <div class="brand-name">Fairpin Links</div>
      <div class="brand-tagline">Play Sharp. Train Smart. Be Better.</div>
    </div>
  </div>
  <p class="description">
    We work with serious golfers and those that want to be serious golfers…<br>
    to make you better, faster, at all phases of the game…<br>
    We use the same state-of-the-art technology as professional golfers…<br>
    which produces data sets that shows your improvement in real time.<br>
    Our facility is available 24/7 to our members, which allows you to improve on your time
  </p>
  <div class="date-box"><span class="accent">MARCH 10TH</span> 1:00-4:00PM</div>
  <p class="email"><span class="accent">Email Us Now</span> info@fairpinlinks.com</p>

  <div class="stamp-box"></div>
  <div class="address-line" style="top:150px"></div>
  <div class="address-line" style="top:183px"></div>
  <div class="address-line" style="top:216px"></div>
  <address class="mailing-address">
    1847 W. Dalton Ave<br>
    <span class="accent">Unit C7</span><br>
    Millbrook, OH 45308<br>
    <span class="accent">www.fairpinlinks.com</span>
  </address>
</section>

<section class="postcard postcard-front">
  <svg class="facility-photo" viewBox="0 0 548 266" role="img" aria-label="Photo of an indoor putting setup with green turf, a putter on a tracking stand and a net">
    <defs>
      <linearGradient id="turfShade" x1="0" y1="0" x2="0" y2="1">
        <stop offset="0" stop-color="#c9cfc6"/>
        <stop offset=".3" stop-color="#5c9455"/>
        <stop offset="1" stop-color="var(--turf)"/>
      </linearGradient>
    </defs>
    <polygon points="380,0 548,0 548,266 380,266 276,142" fill="url(#turfShade)"/>
    <polyline points="380,0 276,142 380,266" fill="none" stroke="var(--red)" stroke-width="3"/>
  </svg>
  <div class="brand">
    <span class="brand-ring"></span>
    <div>
      <div class="brand-name">Fairpin Links</div>
      <div class="brand-tagline">Play Sharp. Train Smart. Be Better.</div>
    </div>
  </div>
  <h2 class="offer-title">OPEN HOUSE SPECIAL</h2>
  <p class="offer-detail">COMPLIMENTARY EVALUATIONS<br>INSTEAD OF $200</p>
  <div class="date-box">MARCH 10TH <span class="accent">1:00-4:00PM</span></div>
  <p class="notice-band">Limited memberships offered. You can email us before the open house to schedule your complimentary evaluation or practice session</p>
  <p class="email"><span class="accent">Email Us Now</span> info@fairpinlinks.com</p>
</section>

</body>
</html>
```